Business cards for the RT Group

We are looking for a template for our new business cards for our company that we can edit ourselves.
You will find our company colors in the logo. the logo on the back and on the front
first name Last Name
position
E-mail address
mobile number
landline number
Companies we have 2 RT Sicherheit GmbH and RT Services GmbH
address
Lindauer Weg 42
22543 Hamburg
www.rtverbund-beispiel.de

Something modern, simple but professional

if you have any questions, bring it on.

Industry/Entity Type

Sicherheit

Contact Information for Business Card

Steht in der Beschreibung

Colors
F0912C
F2A743
F7CA91
FBE8D2
FDF5EE

Requirements
Must have
• recognition value
Nice to have
• professional
Should not have
• Playful

```html
<!DOCTYPE html>
<html lang="de">
<head>
<meta charset="utf-8">
<title>RT Gruppe – Visitenkarten</title>
<link href="https://fonts.googleapis.com/css2?family=Roboto:wght@400;500;700;900&display=swap" rel="stylesheet">
<style>
  :root {
    --bg: #d9d9d9;
    --paper: #ffffff;
    --graphite: #4a4a4a;
    --graphite-dark: #3f3f3f;
    --text: #4d4d4d;
    --orange: #f2700f;
    --rule: #8a8a8a;
    --light: #f2f2f2;
  }
  * { box-sizing: border-box; margin: 0; padding: 0; }
  html, body {
    width: 1200px; height: 800px; overflow: hidden;
    background: var(--bg);
    font-family: "Roboto", Arial, sans-serif;
  }
  .stage {
    width: 1200px; height: 800px;
    display: flex; align-items: center; justify-content: center; gap: 40px;
  }
  .card {
    position: relative;
    width: 540px; height: 330px;
    overflow: hidden;
    box-shadow: 0 6px 18px rgba(0,0,0,.18);
  }

  /* Front */
  .card--front { background: var(--paper); color: var(--text); }
  .brand {
    position: absolute; top: 62px; left: 250px;
    display: flex; align-items: center; gap: 12px;
  }
  .brand__mark { width: 22px; height: 22px; background: var(--orange); }
  .brand__name {
    font-weight: 900; font-size: 40px; letter-spacing: .5px;
    color: var(--graphite); line-height: 1;
  }
  .divider {
    position: absolute; left: 34px; right: 34px; top: 214px;
    height: 1px; background: var(--rule);
  }
  .person { position: absolute; left: 34px; top: 160px; }
  .person__name {
    font-weight: 700; font-size: 22px; letter-spacing: .3px;
    text-transform: uppercase; color: var(--graphite);
  }
  .person__role { font-size: 15px; color: var(--orange); margin-top: 2px; }
  .contact {
    position: absolute; left: 34px; top: 228px;
    list-style: none; font-size: 14px; line-height: 19px;
  }
  .contact li { display: flex; align-items: center; gap: 9px; }
  .contact svg { width: 11px; height: 11px; flex: none; }
  .address {
    position: absolute; right: 34px; top: 146px;
    text-align: right; font-size: 14px; line-height: 19px;
  }
  .address__web { color: var(--orange); }
  .edge {
    position: absolute; left: 0; right: 0; bottom: 0; height: 14px;
    display: flex;
  }
  .edge__graphite { flex: 62; background: var(--graphite); }
  .edge__orange { flex: 38; background: var(--orange); }

  /* Back */
  .card--back {
    background: linear-gradient(160deg, var(--graphite) 0%, var(--graphite-dark) 100%);
    color: var(--light);
  }
  .back-brand {
    position: absolute; top: 118px; left: 0; right: 0;
    display: flex; align-items: center; justify-content: center; gap: 14px;
  }
  .back-brand .brand__mark { width: 26px; height: 26px; background: var(--light); }
  .back-brand .brand__name { color: var(--light); font-size: 46px; }
  .back-web {
    position: absolute; left: 0; right: 0; bottom: 58px;
    text-align: center; font-size: 14px; letter-spacing: 6px;
  }
</style>
</head>
<body>
<main class="stage">

  <section class="card card--front" aria-label="Vorderseite">
    <div class="brand">
      <span class="brand__mark"></span>
      <span class="brand__name">RT Gruppe</span>
    </div>

    <div class="person">
      <p class="person__name">Jonas Berger</p>
      <p class="person__role">President</p>
    </div>

    <address class="address">
      <p>Lindauer Weg 42</p>
      <p>22543 Hamburg</p>
      <p class="address__web">www.rtverbund-beispiel.de</p>
    </address>

    <div class="divider"></div>

    <ul class="contact">
      <li>
        <svg viewBox="0 0 12 12" aria-hidden="true"><path d="M2.5 1 L4.5 1 L5 3.5 L3.8 4.4 Q4.8 6.8 7.6 8.2 L8.5 7 L11 7.5 L11 9.5 Q10.5 11 9 11 Q1 10 1 2.5 Q1 1 2.5 1Z" fill="var(--orange)"/></svg>
        040-555-0142
      </li>
      <li>
        <svg viewBox="0 0 12 12" aria-hidden="true"><rect x="3" y="0.8" width="6" height="10.4" rx="1" fill="none" stroke="var(--orange)" stroke-width="1.4"/></svg>
        0151-555-0187
      </li>
      <li>
        <svg viewBox="0 0 12 12" aria-hidden="true"><rect x="0.5" y="2" width="11" height="8" fill="var(--orange)"/><path d="M0.5 2 L6 6.5 L11.5 2" fill="none" stroke="#fff" stroke-width="1"/></svg>
        berger@rtverbund-beispiel.de
      </li>
    </ul>

    <div class="edge">
      <span class="edge__graphite"></span>
      <span class="edge__orange"></span>
    </div>
  </section>

  <section class="card card--back" aria-label="Rückseite">
    <div class="back-brand">
      <span class="brand__mark"></span>
      <span class="brand__name">RT Gruppe</span>
    </div>
    <p class="back-web">www.rtverbund-beispiel.de</p>
  </section>

</main>
</body>
</html>
```